依頼詳細
味付け海苔は、添付しました写真のような袋に入っており、そこに帯を巻くような形でパッケージしようと考えております。現在その帯に和紙風の紙を使用しようと考案中です。
■ パッケージデザインへの要望

・瀬戸内牛窓産
・澄風庵“こはる”
のキーワードが入り、高級感があるデザイン

■ 商品情報

小袋6枚入り×32袋の味付け海苔

■ パッケージの情報
今回はZIP付きのビニール
サイズ:W185mm × H380mm

上記の袋にH210mmの帯を中央に巻く(幅はビニールの幅と同様)

```html
<!DOCTYPE html>
<html lang="ja">
<head>
<meta charset="utf-8">
<title>澄風庵 こはる 味付け海苔 帯</title>
<link rel="stylesheet" href="https://fonts.googleapis.com/css2?family=Shippori+Mincho:wght@500;700&display=swap">
<style>
  :root {
    --paper: #fbfbfd;
    --frame: #c9ccd4;
    --ink: #1e2a5c;
    --ink-soft: #2c3a74;
    --wave-green: #7cc447;
    --wave-teal: #4fbfcc;
    --wave-blue: #3a64bd;
  }
  * { margin: 0; padding: 0; box-sizing: border-box; }
  html, body { width: 867px; height: 1200px; overflow: hidden; background: #ffffff; }
  .band {
    position: relative;
    width: 867px;
    height: 1200px;
    background: var(--paper);
    font-family: "Shippori Mincho", serif;
    color: var(--ink);
  }
  .band__frame {
    position: absolute;
    inset: 14px;
    border: 3px solid var(--frame);
  }
  .vertical { writing-mode: vertical-rl; position: absolute; }
  .origin {
    top: 140px;
    left: 596px;
    font-size: 52px;
    font-weight: 500;
    line-height: 1;
    letter-spacing: 0.08em;
    color: var(--ink-soft);
  }
  .brand {
    top: 72px;
    left: 370px;
    font-size: 112px;
    font-weight: 700;
    line-height: 1;
    letter-spacing: 0;
  }
  .product {
    top: 450px;
    left: 372px;
    font-size: 106px;
    font-weight: 500;
    line-height: 1;
    letter-spacing: 0.02em;
  }
  .description {
    top: 175px;
    left: 150px;
    font-size: 28px;
    font-weight: 500;
    line-height: 1.5;
    color: var(--ink-soft);
  }
  .wave-ornament {
    position: absolute;
    left: 95px;
    top: 830px;
    width: 757px;
    height: 295px;
    background: linear-gradient(to bottom, var(--wave-green), var(--wave-teal), var(--wave-blue));
    opacity: 0.85;
  }
  .contents {
    position: absolute;
    right: 48px;
    top: 1142px;
    font-size: 28px;
    font-weight: 500;
    line-height: 1;
    letter-spacing: 0.06em;
    color: var(--ink-soft);
  }
</style>
</head>
<body>
  <main class="band">
    <div class="band__frame"></div>

    <p class="vertical origin">瀬戸内牛窓産</p>
    <h1 class="vertical brand">澄風庵</h1>
    <p class="vertical product">こはる</p>

    <p class="vertical description">新海苔を使用、<br>他の味付け海苔よりも<br>焼きを強めに入れているため、<br>「パリッ」と言う食感が強い味付け海苔です。</p>

    <div class="wave-ornament" role="img" aria-label="緑・水色・青の三本の筆で描いた波模様"></div>

    <p class="contents">小袋６枚入り×32袋</p>
  </main>
</body>
</html>
```